Business Card Design Project

Lorantte is a women fashion house focusing on youthful glamour.

We bring together unique designs, premium quality materials and top craftsmanship to deliver sophisticated yet playful glamour, fun and excitement to the confident woman.

We can sum up the brand identity in 3 words:
Glamour – Sophistication – Unique

Industry/Entity Type

Fashion

Requirements
Must have
• Nim Tressoli
nim.tressoli@lorantte-example.com
Mobile: 081 536 2947
Instragram: lorantte_label
Facebook: lorantte

Creative Director
Lorantte Co., LTD
TEL: 02 417 39 86
47 Mango Row, 2nd Floor , D Building , Thonburi Court , Soi Ratchada 29.
Upper Bangrak , Sathorn , Bangkok 10500 Thailand
www.lorantte-example.com

```html
<!DOCTYPE html>
<html lang="en">
<head>
<meta charset="utf-8">
<title>Lorantte — Business Card</title>
<link href="https://fonts.googleapis.com/css2?family=Playfair+Display:wght@400&family=Open+Sans:wght@300;400&display=swap" rel="stylesheet">
<style>
  :root {
    --backdrop: #d9d6d1;
    --card-white: #f7f7f5;
    --ink: #1a1a1a;
    --ink-soft: #5c5c5c;
    --ink-muted: #8d8d8d;
    --band-dark: #0c0c0c;
    --band-mid: #3a3a3a;
    --band-text: #f2f2f2;
    --divider: #b9b9b9;
  }
  * { box-sizing: border-box; margin: 0; padding: 0; }
  html, body { width: 1200px; height: 1000px; overflow: hidden; }
  body {
    background: var(--backdrop);
    display: flex;
    flex-direction: column;
    align-items: center;
    justify-content: center;
    gap: 40px;
    font-family: "Open Sans", Arial, sans-serif;
  }
  .card {
    width: 780px;
    height: 446px;
    position: relative;
    box-shadow: 0 14px 30px rgba(0,0,0,0.28);
  }
  .card--front { background: var(--card-white); }
  .card--back { background: var(--band-dark); }

  .brand-name {
    position: absolute;
    left: 62px;
    top: 200px;
    font-family: "Playfair Display", Georgia, serif;
    font-weight: 400;
    font-size: 76px;
    line-height: 1;
    color: var(--ink);
    letter-spacing: 1px;
  }
  .divider {
    position: absolute;
    left: 400px;
    top: 28px;
    width: 1px;
    height: 326px;
    background: linear-gradient(to bottom, rgba(185,185,185,0), var(--divider) 30%, var(--divider) 70%, rgba(185,185,185,0));
  }
  .person {
    position: absolute;
    left: 440px;
    top: 50px;
  }
  .person__name {
    font-size: 23px;
    font-weight: 400;
    color: var(--ink);
    letter-spacing: 0.5px;
    text-transform: uppercase;
  }
  .person__role {
    font-size: 14px;
    font-weight: 300;
    color: var(--ink-muted);
    margin-top: 2px;
  }
  .contact-list {
    position: absolute;
    left: 440px;
    top: 132px;
    list-style: none;
  }
  .contact-list li {
    display: flex;
    align-items: center;
    gap: 14px;
    font-size: 14px;
    font-weight: 300;
    color: var(--ink-soft);
    height: 32px;
    white-space: nowrap;
  }
  .contact-list svg { width: 16px; height: 16px; flex: none; }
  .address-band {
    position: absolute;
    left: 0;
    bottom: 0;
    width: 100%;
    height: 92px;
    background: linear-gradient(to right, var(--band-mid), var(--band-dark) 45%);
    color: var(--band-text);
    font-size: 15px;
    font-weight: 400;
    line-height: 24px;
    padding: 22px 30px 0 30px;
    white-space: nowrap;
  }
</style>
</head>
<body>
  <section class="card card--front" aria-label="Business card front">
    <div class="brand-name">Lorantte</div>
    <div class="divider"></div>
    <div class="person">
      <div class="person__name">Nim Tressoli</div>
      <div class="person__role">Creative Director</div>
    </div>
    <ul class="contact-list">
      <li>
        <svg viewBox="0 0 16 16" aria-hidden="true"><rect x="1" y="3" width="14" height="10" fill="#1a1a1a"/><path d="M1 3 L8 9 L15 3" stroke="#f7f7f5" stroke-width="1.3" fill="none"/></svg>
        nim.tressoli@lorantte-example.com
      </li>
      <li>
        <svg viewBox="0 0 16 16" aria-hidden="true"><rect x="4" y="1" width="8" height="14" rx="1.5" fill="none" stroke="#1a1a1a" stroke-width="1.6"/><rect x="6" y="12" width="4" height="1.2" fill="#1a1a1a"/></svg>
        081 536 2947
      </li>
      <li>
        <svg viewBox="0 0 16 16" aria-hidden="true"><path d="M3 1.5 L6 1.5 L7 5 L5 6.5 C6 8.8 7.2 10 9.5 11 L11 9 L14.5 10 L14.5 13 C14.5 14 13.5 14.5 12.5 14.5 C6.5 14 2 9.5 1.5 3.5 C1.5 2.5 2 1.5 3 1.5 Z" fill="#1a1a1a"/></svg>
        02 417 39 86
      </li>
      <li>
        <svg viewBox="0 0 16 16" aria-hidden="true"><circle cx="8" cy="8" r="7" fill="#1a1a1a"/><path d="M1 8 H15 M8 1 C5 4 5 12 8 15 M8 1 C11 4 11 12 8 15 M2.5 4.5 H13.5 M2.5 11.5 H13.5" stroke="#f7f7f5" stroke-width="0.9" fill="none"/></svg>
        www.lorantte-example.com
      </li>
      <li>
        <svg viewBox="0 0 16 16" aria-hidden="true"><rect x="2" y="2" width="12" height="12" fill="#1a1a1a"/></svg>
        lorantte_label
      </li>
      <li>
        <svg viewBox="0 0 16 16" aria-hidden="true"><circle cx="8" cy="8" r="6.5" fill="#1a1a1a"/></svg>
        lorantte
      </li>
    </ul>
    <div class="address-band">
      Lorantte Co., LTD - 47 Mango Row, 2nd Floor , D Building , Thonburi Court , Soi Ratchada 29.<br>
      Upper Bangrak , Sathorn , Bangkok 10500 Thailand
    </div>
  </section>
  <section class="card card--back" aria-label="Business card back"></section>
</body>
</html>
```